business card design

i would like business cards designed. My business provides trade qualified personnel to the mining industry to work on heavy mobile equipment.
please put a excavator(digger) in the background in one design and have one design without so i can compare the difference.
also add info:
my logo(attached) and "mobile equipment repair and maintenance"
name: Derek Holloway
address: 57 Tarrowby RD Carmel Perth WA.
mobile: 0438120957
email: derek@ironvalemx.com

```html
<!DOCTYPE html>
<html lang="en">
<head>
<meta charset="utf-8">
<title>Ironvale Maintenance Services – Business Card</title>
<link rel="stylesheet" href="https://fonts.googleapis.com/css2?family=Jost:wght@400;500;600;700;800&display=swap">
<style>
  :root{
    --stage:#07335f;
    --navy:#001e40;
    --paper:#dcdddf;
    --accent:#1a7cf0;
    --ink:#0a1f3c;
  }
  *{margin:0;padding:0;box-sizing:border-box}
  html,body{width:1200px;height:1200px;overflow:hidden}
  body{background:var(--stage);font-family:"Jost",sans-serif;position:relative}

  .card{position:absolute;left:276px;width:651px;height:404px;overflow:hidden}

  /* front */
  .card--front{top:203px;background:var(--navy)}
  .brand{position:absolute;left:0;right:0;text-align:center;font-family:"Jost",sans-serif;font-weight:700;line-height:1}
  .brand__name{display:block;font-size:56px;letter-spacing:1px;font-weight:800}
  .brand__sub{display:block;font-size:14.5px;letter-spacing:1.6px;margin-top:8px;font-weight:800}
  .card--front .brand{top:164px;color:var(--paper)}
  .tagline-band{position:absolute;left:-1px;right:0;top:342px;height:41px;background:var(--paper);
    display:flex;align-items:center;justify-content:center}
  .tagline{font-size:12px;font-weight:700;letter-spacing:5.4px;color:var(--navy)}

  /* back */
  .card--back{top:645px;background:var(--paper)}
  .card--back .brand{left:218px;right:auto;width:396px;top:44px;color:var(--navy)}
  .accent-flag{position:absolute;left:0;top:190px}
  .person{position:absolute;left:41px;top:188px;text-align:right}
  .person__name{font-size:28px;font-weight:700;color:var(--ink);letter-spacing:.8px;line-height:1}
  .person__role{font-size:11px;font-weight:500;letter-spacing:6px;color:var(--ink);margin-top:6px;margin-right:-6px}
  .contacts{position:absolute;left:46px;top:285px;list-style:none}
  .contacts li{display:flex;align-items:center;height:23.5px;font-size:17px;color:var(--ink)}
  .contacts svg{width:18px;height:18px;margin-right:17px;flex:none}
  .footer-band{position:absolute;left:0;right:0;bottom:0;height:21px;background:var(--navy)}
  .footer-stripes{position:absolute;left:510px;bottom:0}
</style>
</head>
<body>

<section class="card card--front" aria-label="Card front">
  <div class="brand">
    <span class="brand__name">IRONVALE</span>
    <span class="brand__sub">MAINTENANCE SERVICES PTY LTD</span>
  </div>
  <div class="tagline-band"><p class="tagline">MOBILE EQUIPMENT REPAIR AND MAINTENANCE</p></div>
</section>

<section class="card card--back" aria-label="Card back">
  <div class="brand">
    <span class="brand__name">IRONVALE</span>
    <span class="brand__sub">MAINTENANCE SERVICES PTY LTD</span>
  </div>

  <svg class="accent-flag" width="21" height="22" viewBox="0 0 21 22" aria-hidden="true">
    <polygon points="0,0 21,0 12,22 0,22" fill="var(--accent)"/>
  </svg>

  <div class="person">
    <p class="person__name">DEREK HOLLOWAY</p>
    <p class="person__role">CHAIRMAN</p>
  </div>

  <ul class="contacts">
    <li>
      <svg viewBox="0 0 18 18" aria-hidden="true"><rect width="18" height="18" rx="6" fill="var(--accent)"/>
        <path d="M5 13V8.5L9 5l4 3.5" fill="none" stroke="#fff" stroke-width="1"/>
        <circle cx="11" cy="11" r="1.8" fill="none" stroke="#fff" stroke-width="1"/></svg>
      57 TARROWBY RD CARMEL PERTH WA
    </li>
    <li>
      <svg viewBox="0 0 18 18" aria-hidden="true"><rect width="18" height="18" rx="6" fill="var(--accent)"/>
        <circle cx="9" cy="9" r="5" fill="none" stroke="#fff" stroke-width="1"/>
        <path d="M7 6.5c0 2.5 2 4.5 4.5 4.5" fill="none" stroke="#fff" stroke-width="1"/></svg>
      0438120957
    </li>
    <li>
      <svg viewBox="0 0 18 18" aria-hidden="true"><rect width="18" height="18" rx="6" fill="var(--accent)"/>
        <circle cx="9" cy="9" r="5" fill="none" stroke="#fff" stroke-width="1"/>
        <text x="9" y="11.2" text-anchor="middle" font-size="6.5" fill="#fff" font-family="Jost, sans-serif">@</text></svg>
      derek@ironvalemx.com
    </li>
  </ul>

  <div class="footer-band"></div>
  <svg class="footer-stripes" width="80" height="21" viewBox="0 0 80 21" aria-hidden="true">
    <polygon points="0,21 11,0 80,0 69,21" fill="var(--paper)"/>
    <polygon points="6,21 17,0 36,0 25,21" fill="var(--accent)"/>
    <polygon points="34,21 45,0 64,0 53,21" fill="var(--accent)"/>
  </svg>
</section>

</body>
</html>
```